sommelier *

Sommelier Wine Hospitality Tavergne Crest experience I'm working as a sommelier in a Tavergne Crest restaurant. I try to reach People who are interested in invest in wine and wine loovers! In terms of color I would like to have a nice color based on a nice bordeaux red (as an advice). By the way i forgot to write my phone number and my email address. 438271905316 kdorvan4@quillpost.net I hope this info is enough so far.

```html
<!DOCTYPE html>
<html lang="en">
<head>
<meta charset="utf-8">
<title>Kasimir Dorvan – Sommelier Business Card</title>
<link rel="stylesheet" href="https://fonts.googleapis.com/css2?family=Barlow+Condensed:wght@600&family=Barlow:wght@500&family=Libre+Bodoni:ital,wght@1,700&display=swap">
<style>
  :root {
    --backdrop: #2a2a2a;
    --card-white: #ffffff;
    --bordeaux: #d9232b;
    --ink: #111111;
    --photo-deep: #2b1424;
    --photo-warm: #c98a5c;
    --photo-rose: #8a4a68;
    --wine-red: #9e1a22;
    --wine-light: #f1e6e6;
  }
  * { margin: 0; padding: 0; box-sizing: border-box; }
  html, body {
    width: 1200px;
    height: 1200px;
    overflow: hidden;
    background: var(--backdrop);
  }
  .canvas {
    position: relative;
    width: 1200px;
    height: 1200px;
  }
  .card {
    position: absolute;
    left: 120px;
    width: 960px;
    height: 520px;
    overflow: hidden;
    box-shadow: 0 18px 40px rgba(0,0,0,0.45);
  }
  .card--front { top: 50px; }
  .card--back { top: 630px; background: var(--card-white); }

  .front-photo {
    position: absolute;
    inset: 0;
    background:
      radial-gradient(circle at 30% 45%, rgba(238,170,110,0.85) 0%, rgba(201,138,92,0.5) 18%, transparent 40%),
      radial-gradient(ellipse at 75% 60%, rgba(180,90,130,0.75) 0%, rgba(138,74,104,0.45) 30%, transparent 60%),
      linear-gradient(120deg, var(--photo-deep) 0%, #4a2434 45%, #3a1c30 100%);
  }
  .front-tagline {
    position: absolute;
    right: 60px;
    bottom: 50px;
    font-family: "Libre Bodoni", serif;
    font-style: italic;
    font-weight: 700;
    font-size: 34px;
    color: var(--card-white);
    letter-spacing: 0.5px;
  }

  .back-photo {
    position: absolute;
    left: 0;
    top: 0;
    width: 400px;
    height: 520px;
    background:
      radial-gradient(ellipse at 55% 72%, rgba(158,26,34,0.9) 0%, rgba(190,60,70,0.55) 22%, transparent 45%),
      linear-gradient(180deg, var(--card-white) 0%, var(--wine-light) 60%, var(--card-white) 100%);
  }
  .contact {
    position: absolute;
    left: 480px;
    top: 190px;
  }
  .contact__name {
    font-family: "Barlow Condensed", sans-serif;
    font-weight: 600;
    font-size: 64px;
    line-height: 1;
    color: var(--bordeaux);
    letter-spacing: 1px;
    text-transform: uppercase;
  }
  .contact__line {
    font-family: "Barlow", sans-serif;
    font-weight: 500;
    font-size: 32px;
    line-height: 1.15;
    color: var(--ink);
  }
</style>
</head>
<body>
<main class="canvas">
  <section class="card card--front">
    <div class="front-photo" role="img" aria-label="Candlelit restaurant table with a glass of rosé wine and pink roses"></div>
    <p class="front-tagline">Tavergne Crest restaurant</p>
  </section>

  <section class="card card--back">
    <div class="back-photo" role="img" aria-label="Red wine being poured into a wine glass"></div>
    <div class="contact">
      <h1 class="contact__name">Kasimir Dorvan</h1>
      <p class="contact__line">sommelier</p>
      <p class="contact__line">+4382-7190-5316</p>
      <p class="contact__line">kdorvan4@quillpost.net</p>
    </div>
  </section>
</main>
</body>
</html>
```